Drink Coaster Design

We will be providing reusable drink coaster for sports bars. The coasters are 4" by 4" with rounded corners. You can see the coasters at this link:
https://www.plumdinersupply.com/4-white-square-80-pt-customizable-paper-coaster-case/771KPLM4Q80.html. We want the coasters to be impressive and lead customers to our web site and our twitter account.
I have included one design created for us but it does not look impressive. We provide information to sports bettors who use our service to decide which games to bet on in college and professional football and basketball. You can see our web site at www.lanternwagerinsights.com. You can see our twitter account at https://twitter.com/lanternforecasts. I have attached several different logos. The goal is to drive traffic to our web site and our twitter account. The design needs to be a conversation "starter" and needs to be impressive. Please visit our web site to understand what we do and to see our key selling points

```html
<!DOCTYPE html>
<html lang="en">
<head>
<meta charset="utf-8">
<title>Lantern Wager Insights – Coaster</title>
<link rel="stylesheet" href="https://fonts.googleapis.com/css2?family=Russo+One&display=swap">
<style>
  :root {
    --red: #e4172b;
    --shadow: #1f2823;
    --green: #2f9b4c;
    --green-light: #49b561;
  }
  html, body {
    margin: 0;
    padding: 0;
    width: 1200px;
    height: 1102px;
    overflow: hidden;
    background: #ffffff;
  }
  .coaster {
    position: relative;
    width: 1200px;
    height: 1102px;
    overflow: hidden;
  }
  .coaster-art {
    position: absolute;
    inset: 0;
    display: block;
  }
  .backdrop-scene { fill: url(#sceneTone); }
  .band { fill: none; stroke: var(--red); }
  .headline {
    font-family: "Russo One", sans-serif;
    fill: var(--red);
  }
  .headline-shadow {
    font-family: "Russo One", sans-serif;
    fill: var(--shadow);
  }
  .brand-name {
    font-family: "Russo One", sans-serif;
    fill: var(--green);
    font-size: 42px;
  }
  .band-text {
    font-family: "Russo One", sans-serif;
    fill: var(--green-light);
    font-size: 40px;
  }
  .band-icon { fill: none; stroke: var(--green-light); stroke-width: 4; }
  .band-dot { fill: var(--green-light); }
</style>
</head>
<body>
<main class="coaster">
  <svg class="coaster-art" viewBox="0 0 1307 1200" width="1200" height="1102" preserveAspectRatio="none" xmlns="http://www.w3.org/2000/svg">
    <defs>
      <linearGradient id="sceneTone" x1="0" y1="0.2" x2="1" y2="0.6">
        <stop offset="0" stop-color="#2c322e"/>
        <stop offset="0.38" stop-color="#59626c"/>
        <stop offset="0.66" stop-color="#bdbcb4"/>
        <stop offset="1" stop-color="#4c8e45"/>
      </linearGradient>
      <path id="bandCurve" d="M -40 600 C 200 1150, 900 1300, 1360 800"/>
    </defs>

    <rect class="backdrop-scene" x="0" y="0" width="1307" height="1200" role="img"
          aria-label="Stylised football boot kicking a soccer ball over green camouflage turf"/>

    <!-- Swooping red bands -->
    <path class="band band-outer" d="M -40 790 C 180 1330, 920 1460, 1360 980" stroke-width="30"/>
    <use class="band band-main" href="#bandCurve" stroke-width="140"/>

    <!-- Brand name -->
    <text class="brand-name" x="58" y="125" textLength="322" lengthAdjust="spacingAndGlyphs">LANTERN WAGER INSIGHTS</text>

    <!-- Headline -->
    <g class="headline-group">
      <text class="headline-shadow" x="478" y="340" font-size="360" textLength="712" lengthAdjust="spacingAndGlyphs">YOU</text>
      <text class="headline" x="490" y="330" font-size="360" textLength="712" lengthAdjust="spacingAndGlyphs">YOU</text>

      <text class="headline-shadow" x="266" y="522" font-size="200" textLength="355" lengthAdjust="spacingAndGlyphs">CAN</text>
      <text class="headline" x="255" y="515" font-size="200" textLength="355" lengthAdjust="spacingAndGlyphs">CAN</text>

      <text class="headline-shadow" x="458" y="870" font-size="380" textLength="705" lengthAdjust="spacingAndGlyphs">WIN</text>
      <text class="headline" x="440" y="860" font-size="380" textLength="705" lengthAdjust="spacingAndGlyphs">WIN</text>
    </g>

    <!-- Globe icon on the band -->
    <g class="band-icon" transform="translate(122 846)">
      <circle r="17"/>
      <ellipse rx="7" ry="17"/>
      <line x1="-17" y1="0" x2="17" y2="0"/>
      <line x1="-14" y1="-9" x2="14" y2="-9"/>
      <line x1="-14" y1="9" x2="14" y2="9"/>
    </g>

    <text class="band-text" dominant-baseline="central">
      <textPath href="#bandCurve" startOffset="325" textLength="680" lengthAdjust="spacingAndGlyphs">www.LANTERNWAGERINSIGHTS.com</textPath>
    </text>

    <circle class="band-dot" cx="886" cy="1084" r="19"/>

    <text class="band-text" dominant-baseline="central">
      <textPath href="#bandCurve" startOffset="1165" textLength="300" lengthAdjust="spacingAndGlyphs">LANTERN FORECASTS</textPath>
    </text>
  </svg>
</main>
</body>
</html>
```